Children's Party Business needs a Business Card design!

We need a double sided, colour business card design.
The company name is "Maplewood Kids' Celebrations". We want one side to feature this logo.
We want the second side to feature the two branches "The Caped Crusade Adventure" and "The Fairytale Gala Adventure". I have attached logos for each of these below. When using these, I suggest removing the tagline & image from the logos, as those elements are already featured in the "Maplewood Kids' Celebration" logo.
To be included:
www.maplewoodkidscelebrations.com.au
1300 471 608
Optional text- "Making Dreams a Reality"
Optional photos- I've attached a bunch of our Character photos, which can be used if you please!
To give you an idea of the business, see The Caped Crusade Adventure website (under development):
http://qorvint.com/demo/capedcrusadeadventure/
Target Market(s)
Parents
Industry/Entity Type
Business
Contact Information for Business Card
To be included:
1300 471 608
Colors
Designer to choose colors to be used in the design.
Look and feel

```html
<!DOCTYPE html>
<html lang="en">
<head>
<meta charset="utf-8">
<title>Maplewood Kids' Celebrations – Business Card</title>
<link href="https://fonts.googleapis.com/css2?family=Varela+Round&display=swap" rel="stylesheet">
<style>
  :root {
    --bg: #111111;
    --card-white: #ffffff;
    --sun-yellow: #fdd325;
    --navy: #2a3870;
    --ink: #2f3a6b;
    --cloud-edge: #d9d9d9;
    --hero-tone: #2d3564;
    --fairy-tone: #8fc6ee;
  }
  * { margin: 0; padding: 0; box-sizing: border-box; }
  html, body {
    width: 1200px; height: 1000px; overflow: hidden;
    background: var(--bg);
    font-family: "Varela Round", sans-serif;
    color: var(--ink);
  }
  .stage {
    position: relative; width: 1200px; height: 1000px;
    display: flex; align-items: center; justify-content: center; gap: 40px;
  }
  .card {
    position: relative; width: 520px; height: 300px;
    border-radius: 22px; overflow: hidden;
  }
  .card-back { background: var(--card-white); }
  .card-front { background: var(--navy); }
  .card svg.cloud { position: absolute; left: 0; top: 0; }
  .branch-name {
    position: absolute; font-size: 19px; color: var(--ink); line-height: 1.1;
  }
  .branch-fairytale { left: 26px; top: 22px; width: 200px; }
  .branch-caped { right: 24px; bottom: 24px; width: 190px; text-align: right; }
  .contact {
    position: absolute; left: 90px; top: 106px; width: 270px; text-align: center;
  }
  .tagline { font-size: 22px; color: var(--ink); white-space: nowrap; }
  .divider { width: 120px; height: 1px; background: var(--ink); margin: 10px auto; opacity: .6; }
  .web, .phone { font-size: 12.5px; color: var(--ink); line-height: 1.5; white-space: nowrap; }
  .hero-art, .fairy-art { position: absolute; border-radius: 36px; }
  .hero-art {
    left: 70px; top: 62px; width: 90px; height: 160px;
    background: linear-gradient(180deg, #e46fa8 0%, #7fb6e0 25%, var(--hero-tone) 45%);
  }
  .fairy-art {
    left: 368px; top: 128px; width: 90px; height: 112px;
    background: linear-gradient(90deg, var(--hero-tone) 45%, var(--fairy-tone) 100%);
  }
  .company-name {
    position: absolute; left: 170px; top: 112px; width: 190px;
    font-size: 24px; line-height: 1.15; color: var(--navy); text-align: center;
  }
</style>
</head>
<body>
<main class="stage">
  <section class="card card-back" aria-label="Card back">
    <svg class="cloud" width="520" height="300" viewBox="0 0 520 300" aria-hidden="true">
      <g fill="var(--sun-yellow)">
        <ellipse cx="225" cy="170" rx="150" ry="80"/>
        <circle cx="150" cy="135" r="62"/>
        <circle cx="245" cy="105" r="65"/>
        <circle cx="320" cy="140" r="58"/>
        <circle cx="140" cy="200" r="55"/>
        <circle cx="300" cy="205" r="55"/>
      </g>
    </svg>
    <p class="branch-name branch-fairytale">The Fairytale Gala Adventure</p>
    <div class="contact">
      <p class="tagline">Making Dreams a Reality</p>
      <div class="divider"></div>
      <p class="web">www.maplewoodkidscelebrations.com.au</p>
      <p class="phone">1300 471 608</p>
    </div>
    <p class="branch-name branch-caped">The Caped Crusade Adventure</p>
  </section>

  <section class="card card-front" aria-label="Card front">
    <svg class="cloud" width="520" height="300" viewBox="0 0 520 300" aria-hidden="true">
      <g fill="var(--card-white)" stroke="var(--cloud-edge)" stroke-width="3">
        <ellipse cx="260" cy="165" rx="215" ry="100"/>
        <circle cx="160" cy="110" r="70"/>
        <circle cx="270" cy="90" r="78"/>
        <circle cx="375" cy="115" r="68"/>
        <circle cx="170" cy="215" r="60"/>
        <circle cx="350" cy="215" r="62"/>
      </g>
      <g fill="var(--card-white)">
        <ellipse cx="260" cy="165" rx="213" ry="98"/>
        <circle cx="160" cy="110" r="68"/>
        <circle cx="270" cy="90" r="76"/>
        <circle cx="375" cy="115" r="66"/>
        <circle cx="170" cy="215" r="58"/>
        <circle cx="350" cy="215" r="60"/>
      </g>
    </svg>
    <div class="hero-art" role="img" aria-label="Silhouette of a superhero holding party balloons"></div>
    <p class="company-name">Maplewood Kids' Celebrations</p>
    <div class="fairy-art" role="img" aria-label="Silhouette of a leaping fairy with light blue wings"></div>
  </section>
</main>
</body>
</html>
```